Letterhead

Can you please design me a letterhead that I can use electronically in word as a template. I have attached my business card as I would like the design to reflect this logo.

```html
<!DOCTYPE html>
<html lang="en">
<head>
<meta charset="utf-8">
<title>Meridale Business Consultants – Letterhead</title>
<link rel="stylesheet" href="https://fonts.googleapis.com/css2?family=Arimo:wght@400&family=Source+Sans+3:wght@400;600&display=swap">
<style>
  :root {
    --brand-red: #9b2335;
    --text-grey: #4a4a4a;
    --paper: #ffffff;
    --divider: #9b2335;
  }
  html, body {
    margin: 0;
    padding: 0;
    overflow: hidden;
    background: var(--paper);
  }
  .letterhead {
    position: relative;
    width: 849px;
    height: 1200px;
    box-sizing: border-box;
    border: 1px solid var(--brand-red);
    background: var(--paper);
    overflow: hidden;
  }
  .brand {
    position: absolute;
    left: 38px;
    top: 26px;
  }
  .brand-name {
    margin: 0;
    font-family: "Arimo", Arial, sans-serif;
    font-weight: 400;
    font-size: 76px;
    line-height: 1;
    letter-spacing: 1px;
    color: var(--brand-red);
  }
  .brand-descriptor {
    margin: 8px 0 0 4px;
    font-family: "Arimo", Arial, sans-serif;
    font-size: 15px;
    color: var(--text-grey);
  }
  .contact-footer {
    position: absolute;
    left: 0;
    right: 0;
    top: 1164px;
    text-align: center;
    font-family: "Source Sans 3", "Myriad Pro", sans-serif;
    font-size: 11.5px;
    color: var(--text-grey);
    white-space: nowrap;
  }
  .contact-footer .label {
    color: var(--brand-red);
  }
  .contact-footer .principal-name {
    font-weight: 600;
    font-size: 13px;
    margin-left: 4px;
  }
  .contact-footer .sep {
    color: var(--divider);
    margin: 0 5px;
  }
</style>
</head>
<body>
  <div class="letterhead">
    <header class="brand">
      <h1 class="brand-name">meridale</h1>
      <p class="brand-descriptor">Business Consultants Pty Ltd</p>
    </header>

    <footer class="contact-footer">
      <span class="label">Principal</span><span class="principal-name">Helen Carwright</span>
      <span class="sep">|</span><span class="label">P :</span> 0400 555 018
      <span class="sep">|</span><span class="label">E :</span> helen@meridale net au
      <span class="sep">|</span><span class="label">ACN :</span> 000 123 456
    </footer>
  </div>
</body>
</html>
```